Fantasy Sports Website re-Design

We need a website designed for our fantasy sports website. The website is GridVortez.com . An example of the website layout would be like : https://www.kormadyne.com/fantasy-sports/fantasy-sports-solutions. We like this site, because of the screenshots on 1 side and a description on the other side. This layout style will showcase the features we have on our site. Somewhere in the header there will be a video explaining what the site is. We would like the style to be black and gold. Like a casino. Attached is an example logo to give the style we want.

Target Market(s)

fantasy sports

Number of Pages Required

3 page

Colors
fecb35
000000

Requirements
Must have
• mockups of index page
Nice to have
• mockups of sub pages

```html
<!DOCTYPE html>
<html lang="en">
<head>
<meta charset="utf-8">
<title>GridVortez.com – Crypto Fantasy Sports</title>
<link href="https://fonts.googleapis.com/css2?family=Open+Sans:wght@400;600;700&display=swap" rel="stylesheet">
<style>
:root{
  --gold:#fecb35;
  --gold-deep:#e2ad12;
  --black:#000000;
  --header:#121212;
  --night:#1c2333;
  --footer:#252525;
  --bar:#1e1e1e;
  --panel:#e9e9e9;
  --tab:#d6d6d6;
  --muted:#a9a9a9;
  --white:#ffffff;
}
*{box-sizing:border-box;margin:0;padding:0}
html,body{width:697px;height:1200px;overflow:hidden;background:var(--black);font-family:"Open Sans",Arial,sans-serif;color:var(--white)}
.page{position:relative;width:697px;height:1200px}
.site-header{position:absolute;top:0;left:0;width:697px;height:92px;background:var(--header)}
.brand{position:absolute;left:77px;top:30px;font-size:26px;font-weight:700;color:var(--gold);letter-spacing:1px}
.actions{position:absolute;right:77px;top:24px;display:flex;gap:5px}
.btn{font-size:7.5px;font-weight:600;height:20px;line-height:20px;padding:0 9px;border-radius:2px;text-transform:uppercase}
.btn-outline{border:1px solid #777;color:var(--white);display:flex;align-items:center;gap:4px}
.btn-gold{background:var(--gold);color:var(--black)}
.main-nav{position:absolute;right:77px;top:63px;display:flex;gap:19px;font-size:7.5px;color:#bbb;text-transform:uppercase}
.main-nav .active{color:var(--white)}
.hero{position:absolute;top:92px;left:0;width:697px;height:265px;background:radial-gradient(ellipse at 50% 40%,#5c4a32 0%,#2a241c 45%,#0d0d0d 100%)}
.hero-photo{position:absolute;inset:0;background:linear-gradient(180deg,rgba(0,0,0,0) 60%,rgba(52,74,40,.55) 100%)}
.hero-play{position:absolute;left:334px;top:97px}
.hero h1{position:absolute;top:133px;width:100%;text-align:center;font-size:19px;font-weight:700;letter-spacing:.2px}
.hero p{position:absolute;top:158px;width:100%;text-align:center;font-size:9.5px}
.featured{position:absolute;top:357px;left:0;width:697px;height:278px;background:linear-gradient(180deg,#222a38 0%,#2c3442 55%,#3c5a2a 80%,#2a3a20 100%)}
.section-title{position:absolute;width:100%;text-align:center;font-size:19px;font-weight:700;color:var(--gold-deep)}
.featured .section-title{top:30px}
.game-card{position:absolute;top:63px;width:172px;height:148px}
.game-card .photo{height:116px}
.game-card .label{height:32px;line-height:32px;text-align:center;font-size:13.5px;font-weight:700;color:#111;background:linear-gradient(180deg,var(--gold),var(--gold-deep))}
.carousel{position:absolute;top:225px;left:327px;display:flex;gap:6px}
.lobby{position:absolute;top:635px;left:0;width:697px;height:370px;background:linear-gradient(180deg,#1c2333 0%,#262b38 50%,#2c261f 100%)}
.lobby .section-title{top:42px}
.filters{position:absolute;left:77px;top:79px;width:126px}
.filter-head{height:26px;background:var(--gold);color:#111;font-size:9.5px;font-weight:600;padding:0 8px;display:flex;justify-content:space-between;align-items:center}
.league-list{background:var(--panel);list-style:none;padding:7px 8px;height:108px;border-bottom:2px solid #bbb}
.league-list li{color:#333;font-size:6.5px;height:18.6px;line-height:18.6px}
.filter-tab{margin-top:2px;height:26px;background:var(--tab);color:#222;font-size:9.5px;padding:0 8px;display:flex;justify-content:space-between;align-items:center}
.sport-tile{position:absolute;width:130px;height:118px}
.sport-tile span{position:absolute;bottom:8px;width:100%;text-align:center;font-size:9.5px;font-weight:600}
.site-footer{position:absolute;top:1005px;left:0;width:697px;height:140px;background:var(--footer)}
.footer-col{position:absolute;top:32px}
.footer-col h3{font-size:9.5px;font-weight:600;color:var(--gold-deep);margin-bottom:9px}
.footer-col li{list-style:none;font-size:6.5px;color:var(--muted);line-height:14px}
.disclaimer p{width:255px;font-size:5.2px;line-height:10px;color:var(--muted)}
.bottom-bar{position:absolute;top:1145px;left:0;width:697px;height:55px;background:var(--bar)}
.bottom-nav{position:absolute;left:77px;top:17px;font-size:6px;color:var(--muted)}
.copyright{position:absolute;left:77px;top:33px;font-size:6px;color:var(--muted)}
.social{position:absolute;right:77px;top:20px;display:flex;gap:4px}
.social i{width:15px;height:15px;border-radius:50%;display:block}
</style>
</head>
<body>
<div class="page">
  <header class="site-header">
    <div class="brand">GRID VORTEZ</div>
    <div class="actions">
      <span class="btn btn-outline"><svg width="7" height="7" viewBox="0 0 10 10"><circle cx="5" cy="5" r="4.3" fill="none" stroke="#fff"/><path d="M4 3l3 2-3 2z" fill="#fff"/></svg>View Demo Video</span>
      <span class="btn btn-gold">Sign Up</span>
      <span class="btn btn-gold">Login</span>
    </div>
    <nav class="main-nav">
      <span class="active">Fantasy</span><span>Lobby</span><span>Statistics</span><span>Referral</span><span>Mobile App</span><span>Documentation</span>
    </nav>
  </header>

  <section class="hero">
    <div class="hero-photo" role="img" aria-label="Soccer players chasing the ball in a floodlit stadium"></div>
    <svg class="hero-play" width="29" height="29" viewBox="0 0 30 30"><circle cx="15" cy="15" r="14" fill="#fff"/><path d="M12 9l9 6-9 6z" fill="#111"/></svg>
    <h1>THE LEADER IN CRYPTO FANTASY SPORTS</h1>
    <p>Use Crypto Currencies to play against users from all over the world!</p>
  </section>

  <section class="featured">
    <h2 class="section-title">FEATURED GAMES</h2>
    <div class="game-card" style="left:77px"><div class="photo" role="img" aria-label="Soccer player striking a ball at sunset" style="background:linear-gradient(180deg,#6f6a6c,#c08a4c 55%,#3d5a2a)"></div><div class="label">SOCCER</div></div>
    <div class="game-card" style="left:262px"><div class="photo" role="img" aria-label="Basketball player dunking in an arena" style="background:linear-gradient(180deg,#14141c,#3a2630 60%,#1a1a22)"></div><div class="label">BASKET BALL</div></div>
    <div class="game-card" style="left:447px"><div class="photo" role="img" aria-label="Golfer swinging on a green course" style="background:linear-gradient(180deg,#b7d0e6,#8fae5a 55%,#5f8a34)"></div><div class="label">GOLF</div></div>
    <div class="carousel">
      <svg width="18" height="18" viewBox="0 0 20 20"><circle cx="10" cy="10" r="10" fill="#fecb35"/><path d="M12 5l-5 5 5 5" fill="none" stroke="#222" stroke-width="2.2"/></svg>
      <svg width="18" height="18" viewBox="0 0 20 20"><circle cx="10" cy="10" r="10" fill="#999"/><path d="M8 5l5 5-5 5" fill="none" stroke="#333" stroke-width="2.2"/></svg>
    </div>
  </section>

  <section class="lobby">
    <h2 class="section-title">GAME LOBBY</h2>
    <aside class="filters">
      <div class="filter-head">LEAGUE SELECTION <svg width="9" height="9" viewBox="0 0 10 10"><circle cx="5" cy="5" r="5" fill="#111"/><path d="M2.5 5h5" stroke="#fecb35" stroke-width="1.4"/></svg></div>
      <ul class="league-list">
        <li>› Vestibulum</li><li>› Mauris bibendum</li><li>› Cras eget</li><li>› Aliquam erat</li><li>› Nulla tristique</li>
      </ul>
      <div class="filter-tab">SPORT <svg width="9" height="9" viewBox="0 0 10 10"><circle cx="5" cy="5" r="5" fill="#666"/><path d="M2.5 5h5M5 2.5v5" stroke="#fff" stroke-width="1.3"/></svg></div>
      <div class="filter-tab">ENTRY FEE <svg width="9" height="9" viewBox="0 0 10 10"><circle cx="5" cy="5" r="5" fill="#666"/><path d="M2.5 5h5M5 2.5v5" stroke="#fff" stroke-width="1.3"/></svg></div>
      <div class="filter-tab">SIZE OF POOL <svg width="9" height="9" viewBox="0 0 10 10"><circle cx="5" cy="5" r="5" fill="#666"/><path d="M2.5 5h5M5 2.5v5" stroke="#fff" stroke-width="1.3"/></svg></div>
      <div class="filter-tab">MORE FILTERS <svg width="9" height="9" viewBox="0 0 10 10"><circle cx="5" cy="5" r="5" fill="#666"/><path d="M2.5 5h5M5 2.5v5" stroke="#fff" stroke-width="1.3"/></svg></div>
    </aside>
    <div class="sport-tile" role="img" aria-label="Handball player leaping to throw" style="left:213px;top:79px;background:linear-gradient(180deg,#5b6a5e,#3a3f3c 60%,#0c0c0c)"><span>HANDBALL</span></div>
    <div class="sport-tile" role="img" aria-label="Ice hockey team lined up on the rink" style="left:351px;top:79px;background:linear-gradient(180deg,#6f7b88,#8a3a38 55%,#0c0c0c)"><span>ICE HOCKEY</span></div>
    <div class="sport-tile" role="img" aria-label="Tennis player returning a shot on court" style="left:489px;top:79px;background:linear-gradient(180deg,#3c5a48,#6a7a6a 55%,#0c0c0c)"><span>TENNIS</span></div>
    <div class="sport-tile" role="img" aria-label="Fighters in a mixed martial arts cage" style="left:213px;top:206px;background:linear-gradient(180deg,#2a3040,#7a808c 55%,#0c0c0c)"><span>MMA</span></div>
    <div class="sport-tile" role="img" aria-label="American football player in helmet" style="left:351px;top:206px;background:linear-gradient(180deg,#3a3020,#2a2a3a 55%,#0c0c0c)"><span>FOOT BALL</span></div>
    <div class="sport-tile" role="img" aria-label="Formula one car racing on a track" style="left:489px;top:206px;background:linear-gradient(180deg,#6f9ad0,#3a6ab0 55%,#0c0c0c)"><span>F1 CAR RACE</span></div>
  </section>

  <footer class="site-footer">
    <div class="footer-col" style="left:77px"><h3>Quick Links</h3><ul><li>My Live Games</li><li>My Upcoming Games</li><li>My History Games</li><li>My Account</li></ul></div>
    <div class="footer-col" style="left:182px"><h3>Resources</h3><ul><li>My Profile</li><li>Future Events</li><li>Withdrawal History</li><li>Transactions</li></ul></div>
    <div class="footer-col" style="left:281px"><h3>Sublinks</h3><ul><li>Game Summery</li><li>My Funds</li><li>Add Funds</li><li>Create Contest</li></ul></div>
    <div class="footer-col disclaimer" style="left:364px"><h3>Legal Discalimer</h3>
      <p>This site is a Game of Skill and is 100% LEGAL in the United States. This site operates in full compliance with the Unlawful Internet Gambling Enforcement Act of 2006. This site does not encourage unlawful gambling in any way, shape or form. Due to state and provincial law residents of Arizona, Iowa, Louisiana, Montana, Vermont and Quebec may only play in free competitions. All other trademarks and logos belong to their respective owners. PLAYMERIDIAN.COM Fantasy Sports</p>
    </div>
  </footer>
  <div class="bottom-bar">
    <div class="bottom-nav">Fantasy &nbsp;|&nbsp; Lobby &nbsp;|&nbsp; Statistics &nbsp;|&nbsp; Referral &nbsp;|&nbsp; Mobile App &nbsp;|&nbsp; Documentation</div>
    <div class="copyright">Copyright © 2018 GRID VORTEZ. All Rights Reserved</div>
    <div class="social"><i style="background:#3b5a9a"></i><i style="background:#2ea3e8"></i></div>
  </div>
</div>
</body>
</html>
```